The Harvest Of Quiet Fields Inc.

On one side have the business name. On the other side have contact information. This is an indoor cannabis cultivation business. It’s a new company in Sacramento ca. So we need a logo designed. The company is Called the harvest of quiet fields. We grow and distribute marijuana in California. We would like to see designers use the color green and communicate cultivation.

Target Market(s)

Networking

Contact Information for Business Card

Dale Crennick: president
Phone: (916) 555-0173
Email: dale@theharvestofquietfields.net

Logo Text

Not sure if i want text or just an image created by designers.

Font styles to use
Script

Colors
000000
9bcb3c
fbfcf7
cadf82

Requirements
Nice to have
• A classic elegant professional card.

```html
<!DOCTYPE html>
<html lang="en">
<head>
<meta charset="utf-8">
<title>The Harvest Of Quiet Fields Inc. — Business Card</title>
<link rel="stylesheet" href="https://fonts.googleapis.com/css2?family=Arimo:wght@400;700&display=swap">
<style>
  :root {
    --stage: #e9e7e1;
    --card: #fbfcf7;
    --green-deep: #178a4f;
    --green-soft: #74bf86;
    --teal: #6aa9a6;
    --ink-soft: #5e9e80;
  }
  * { margin: 0; padding: 0; box-sizing: border-box; }
  html, body { width: 900px; height: 1200px; overflow: hidden; }
  body {
    position: relative;
    background: var(--stage);
    font-family: "Arimo", Arial, sans-serif;
  }
  .card {
    position: absolute;
    left: 80px;
    width: 733px;
    height: 428px;
    background: var(--card);
    border-radius: 24px;
    box-shadow: 0 6px 16px rgba(0,0,0,0.18);
  }
  .card--front { top: 128px; }
  .card--back { top: 646px; }

  .brand {
    position: absolute;
    text-align: center;
    transform: translateX(-50%);
  }
  .brand__mark {
    display: block;
    width: 120px;
    height: 120px;
    margin: 0 auto 26px;
    border-radius: 50%;
    background: var(--green-deep);
  }
  .brand__name {
    display: block;
    font-weight: 700;
    font-size: 23px;
    color: var(--green-deep);
    white-space: nowrap;
    letter-spacing: -0.2px;
  }
  .brand__tagline {
    display: block;
    margin-top: 6px;
    font-size: 11.5px;
    color: var(--green-soft);
    white-space: nowrap;
  }
  .card--front .brand { left: 366px; top: 114px; }
  .card--back .brand { left: 212px; top: 116px; }

  .divider {
    position: absolute;
    left: 396px;
    top: 94px;
    width: 1.5px;
    height: 240px;
    background: var(--teal);
  }
  .contact {
    position: absolute;
    left: 422px;
    top: 160px;
  }
  .contact__name {
    font-weight: 700;
    font-size: 21px;
    color: var(--green-deep);
    letter-spacing: 0.6px;
  }
  .contact__role {
    margin-top: 5px;
    font-size: 15px;
    color: var(--green-soft);
    letter-spacing: 0.5px;
  }
  .contact__list { list-style: none; margin-top: 22px; }
  .contact__item {
    display: flex;
    align-items: center;
    gap: 10px;
    font-size: 15.5px;
    color: var(--green-deep);
    margin-bottom: 9px;
  }
  .contact__icon { width: 17px; height: 17px; flex: none; fill: var(--ink-soft); }
</style>
</head>
<body>
  <section class="card card--front">
    <div class="brand">
      <span class="brand__mark"></span>
      <span class="brand__name">The Harvest Of Quiet Fields Inc.</span>
      <span class="brand__tagline">Grow and distribute marijuana in California</span>
    </div>
  </section>

  <section class="card card--back">
    <div class="brand">
      <span class="brand__mark"></span>
      <span class="brand__name">The Harvest Of Quiet Fields Inc.</span>
      <span class="brand__tagline">Grow and distribute marijuana in California</span>
    </div>
    <div class="divider"></div>
    <div class="contact">
      <p class="contact__name">DALE CRENNICK</p>
      <p class="contact__role">PRESIDENT</p>
      <ul class="contact__list">
        <li class="contact__item">
          <svg class="contact__icon" viewBox="0 0 24 24" aria-hidden="true"><path d="M6.6 10.8a15.1 15.1 0 0 0 6.6 6.6l2.2-2.2c.3-.3.7-.4 1-.2 1.1.4 2.3.6 3.6.6.6 0 1 .4 1 1V20c0 .6-.4 1-1 1C10.6 21 3 13.4 3 4c0-.6.4-1 1-1h3.5c.6 0 1 .4 1 1 0 1.3.2 2.5.6 3.6.1.3 0 .7-.2 1z"/></svg>
          <span>(916) 555-0173</span>
        </li>
        <li class="contact__item">
          <svg class="contact__icon" viewBox="0 0 24 24" aria-hidden="true"><path d="M2 5h20v14H2z" fill="none"/><path d="M2 5h20v2l-10 6L2 7z"/><path d="M2 9l10 6 10-6v10H2z"/></svg>
          <span>dale@theharvestofquietfields.net</span>
        </li>
      </ul>
    </div>
  </section>
</body>
</html>
```